Pinnacrest Hotel Management Consulting Solutions needs website design.

I need a clear simple website design for a new company in Western Australia providing Hotel Management expertise through consulting services / solutions / advice. I have a logo and need a website designed. I would like the logo to be the hero of the website. I would like modern, cutting edge design to reflect the professional service I will be supplying. See logo attached to assist (in website files). The purpose of the website is to inform basic business information linking to my email addresses, including Facebook and Instagram. I want to show that my services can benefit all private and commercial hotel / resort / type businesses using my vast 25 years international Hotel experience from 3 star to 5 star hotels and resorts with a respected hotel group, to grow their business or trouble shooting. Key Services, through a menu bar to include, Hotel 360 Operations, Hotel Budgeting / Business Plans, Business Strategies, Revenue Management, Financial advice, Cost Management Solutions, Pre-Opening Hotel Overview, Hotel Marketing, Investor Communications Support, Asset Management, Hotel Real Estate Investment advice, People Management. I want the menu bar titles to include About me, showing my experience, Hotel 360 Services (to then drop down to all the above hotel services, then drop down to a brief description of each hotel department), Contact details, etc.

```html
<!DOCTYPE html>
<html lang="en">
<head>
<meta charset="utf-8">
<title>Pinnacrest Hotel Management Consulting Solutions</title>
<link href="https://fonts.googleapis.com/css2?family=Montserrat:wght@700;800&family=PT+Sans:wght@400;700&family=Poppins:wght@400;500&display=swap" rel="stylesheet">
<style>
:root{
  --navy:#18213a;
  --navy-2:#222c47;
  --ink:#1c2235;
  --body:#3b4054;
  --tint:#eef2fb;
  --white:#ffffff;
  --line:#5d6478;
}
*{margin:0;padding:0;box-sizing:border-box}
html,body{width:1200px;height:4451px;overflow:hidden;background:var(--white)}
body{position:relative;font-family:"Poppins",sans-serif;color:var(--ink)}
.abs{position:absolute}
.heading{font-family:"PT Sans",sans-serif;font-weight:700;text-transform:uppercase;color:var(--ink)}
.center{text-align:center}
/* header */
.site-header{left:0;top:0;width:1200px;height:150px;background:var(--white);z-index:3}
.brand{left:160px;top:-60px;width:240px;height:280px;border-radius:0 0 120px 120px;background:var(--white);z-index:4;display:flex;align-items:flex-end;justify-content:center;padding-bottom:52px}
.brand-name{font-family:"PT Sans",sans-serif;font-weight:700;font-size:12px;line-height:14px;color:var(--navy);text-align:center;text-transform:uppercase;width:200px}
.contact-mail{left:650px;top:30px;display:flex;align-items:center;gap:12px}
.mail-icon{width:40px;height:40px;border-radius:50%;background:var(--navy);display:flex;align-items:center;justify-content:center}
.mail-text small{display:block;font-size:14px;color:var(--ink);line-height:18px}
.mail-text span{font-size:19px;font-weight:500;color:var(--ink)}
.social{left:948px;top:30px;display:flex;gap:6px}
.social span{width:36px;height:36px;border-radius:50%;background:var(--navy)}
.nav{left:495px;top:100px;display:flex;gap:31px;font-family:"PT Sans",sans-serif;font-size:15px;text-transform:uppercase;color:var(--ink)}
/* hero */
.hero{left:0;top:150px;width:1200px;height:671px;background:linear-gradient(180deg,#5a3a33 0%,#8b6f63 35%,#b9b4b0 55%,#7a6a62 75%,#4a3a35 100%)}
.hero-band{left:268px;top:334px;width:666px;height:167px;background:rgba(255,255,255,.7)}
.hero-title{left:200px;top:372px;width:800px;font-family:"Montserrat",sans-serif;font-weight:800;font-size:37px;line-height:45px;color:var(--navy);text-align:center;text-transform:uppercase;letter-spacing:.5px}
.type-card{border-radius:50%;background:var(--white);border:2px solid var(--navy);box-shadow:0 6px 14px rgba(0,0,0,.2);overflow:hidden;text-align:center}
.type-card .cap{position:absolute;left:50%;transform:translateX(-50%);border-radius:50%;background:var(--navy);display:flex;align-items:center;justify-content:center}
.type-card h3{position:absolute;left:0;right:0;font-family:"PT Sans",sans-serif;font-weight:700;font-size:19px;text-transform:uppercase;color:var(--ink)}
.type-card p{position:absolute;left:40px;right:40px;font-size:12px;line-height:20px;color:var(--body)}
.type-card.dark{background:var(--navy);border-color:var(--white)}
.type-card.dark .cap{background:var(--white)}
.type-card.dark h3,.type-card.dark p{color:var(--white)}
/* intro */
.section-title{font-size:27px;letter-spacing:.3px}
.lead{font-size:12px;line-height:26px;color:var(--body)}
.service-card{width:273px;overflow:hidden;color:var(--white);text-align:center}
.service-card .label{position:absolute;left:0;right:0;bottom:18px}
.service-card h4{font-family:"PT Sans",sans-serif;font-weight:700;font-size:19px;text-transform:uppercase;margin-bottom:6px}
.service-card p{font-size:13px;line-height:21px;padding:0 20px}
/* services */
.services-band{left:0;top:1793px;width:1200px;height:688px;background:var(--tint)}
.service-item{left:173px;display:flex;align-items:center;gap:24px}
.item-icon{width:82px;height:82px;border-radius:50%;background:var(--navy);border:4px solid var(--white);box-shadow:0 3px 8px rgba(0,0,0,.25);display:flex;align-items:center;justify-content:center;flex:none}
.service-item h5{font-family:"PT Sans",sans-serif;font-weight:700;font-size:18px;text-transform:uppercase;color:var(--ink);margin-bottom:6px}
.service-item p{font-size:13px;color:var(--body)}
/* expertise */
.expert{border-radius:50%;border:3px solid var(--white);box-shadow:0 6px 16px rgba(0,0,0,.25);display:flex;align-items:center;justify-content:center}
.expert span{width:62%;height:62%;border-radius:50%;background:rgba(90,98,120,.55);display:flex;align-items:center;justify-content:center;text-align:center;font-family:"PT Sans",sans-serif;font-size:18px;line-height:26px;text-transform:uppercase;color:var(--white)}
/* contact */
.contact-band{left:0;top:3230px;width:1200px;height:652px;background:var(--tint)}
.field{left:653px;width:374px;height:55px;border:1px solid var(--ink);background:var(--white);font-size:13px;padding:18px 12px;color:var(--ink)}
.submit{left:653px;top:3726px;width:108px;height:54px;background:var(--navy);color:var(--white);font-family:"PT Sans",sans-serif;font-weight:700;font-size:14px;display:flex;align-items:center;justify-content:center}
/* footer */
.footer{left:0;top:3882px;width:1200px;height:569px;background:var(--navy);color:var(--white)}
.foot-icon{width:72px;height:72px;border-radius:50%;border:2px solid var(--white);display:flex;align-items:center;justify-content:center}
.foot-title{font-family:"PT Sans",sans-serif;font-weight:700;font-size:19px;text-transform:uppercase;color:var(--white)}
.foot-text{font-size:12px;line-height:25px;color:var(--white)}
.foot-brand{font-family:"PT Sans",sans-serif;font-weight:700;font-size:18px;line-height:22px;text-transform:uppercase;color:var(--white);text-align:center}
</style>
</head>
<body>

<header class="site-header abs">
  <div class="brand abs"><div class="brand-name">Pinnacrest Hotel Management Consulting Solutions</div></div>
  <div class="contact-mail abs">
    <div class="mail-icon"><svg width="20" height="14" viewBox="0 0 20 14"><rect x="1" y="1" width="18" height="12" fill="none" stroke="#fff" stroke-width="1.5"/><path d="M1 1l9 7 9-7" fill="none" stroke="#fff" stroke-width="1.5"/></svg></div>
    <div class="mail-text"><small>Email:</small><span>info@pinnacresthm.com</span></div>
  </div>
  <div class="social abs" aria-label="Social links"><span></span><span></span></div>
  <nav class="nav abs"><span>Home</span><span>About me</span><span>Showing my experience</span><span>Hotel 360 services</span></nav>
</header>

<div class="hero abs" role="img" aria-label="Photo of a modern hotel lobby lounge with leather sofas and chandeliers"></div>
<div class="hero-band abs"></div>
<h1 class="hero-title abs">Pinnacrest Hotel Management<br>Consulting - Solutions</h1>

<div class="type-card abs" style="left:174px;top:652px;width:270px;height:270px">
  <div class="cap" style="top:-2px;width:150px;height:150px;margin-top:-28px"><svg width="50" height="60" viewBox="0 0 50 60"><rect x="8" y="6" width="24" height="50" fill="none" stroke="#fff" stroke-width="2"/><rect x="32" y="24" width="12" height="32" fill="none" stroke="#fff" stroke-width="2"/><g fill="#fff"><rect x="13" y="12" width="5" height="5"/><rect x="22" y="12" width="5" height="5"/><rect x="13" y="22" width="5" height="5"/><rect x="22" y="22" width="5" height="5"/><rect x="13" y="32" width="5" height="5"/><rect x="22" y="32" width="5" height="5"/></g></svg></div>
  <h3 style="top:148px">Private Hotel</h3>
  <p style="top:184px">Duis aute irure dolor in reprehenderit in voluptate velit esse</p>
</div>
<div class="type-card dark abs" style="left:453px;top:674px;width:294px;height:294px">
  <div class="cap" style="top:-2px;width:160px;height:160px;margin-top:-45px"><svg width="58" height="70" viewBox="0 0 58 70"><path d="M29 3C15 3 5 13 5 27c0 17 24 40 24 40s24-23 24-40C53 13 43 3 29 3z" fill="var(--navy)"/><circle cx="29" cy="27" r="14" fill="#fff"/><rect x="21" y="24" width="16" height="8" rx="2" fill="var(--navy)"/></svg></div>
  <h3 style="top:170px">Resort</h3>
  <p style="top:206px">Duis aute irure dolor in reprehenderit in voluptate velit esse</p>
</div>
<div class="type-card abs" style="left:756px;top:652px;width:270px;height:270px">
  <div class="cap" style="top:-2px;width:150px;height:150px;margin-top:-28px"><svg width="64" height="62" viewBox="0 0 64 62"><g fill="#fff"><circle cx="20" cy="4" r="2"/><circle cx="27" cy="4" r="2"/><circle cx="34" cy="4" r="2"/><circle cx="41" cy="4" r="2"/></g><rect x="10" y="10" width="44" height="48" fill="none" stroke="#fff" stroke-width="2"/><g fill="#fff"><rect x="16" y="16" width="32" height="3"/><rect x="16" y="24" width="32" height="3"/><rect x="16" y="32" width="32" height="3"/><rect x="27" y="42" width="10" height="16"/></g></svg></div>
  <h3 style="top:148px">Commercial Hotel</h3>
  <p style="top:184px">Duis aute irure dolor in reprehenderit in voluptate velit esse</p>
</div>

<h2 class="heading section-title abs center" style="left:0;top:1070px;width:1200px">Pinnacrest Hotel Management Consulting</h2>
<p class="lead abs center" style="left:170px;top:1128px;width:860px">Nemo enim ipsam voluptatem quia voluptas sit aspernatur aut odit aut fugit, sed quia consequuntur magni dolores eos qui ratione voluptatem sequi nesciunt. Neque porro quisquam est, qui dolorem ipsum quia dolor sit amet, consectetur, adipisci velit, sed quia non numquam eius modi tempora incidunt ut labore et dolore magnam aliquam quaerat voluptatem.</p>

<div class="service-card abs" style="left:29px;top:1307px;height:356px;background:linear-gradient(180deg,#8a6a4f 0%,#6b5240 50%,#2a2420 100%)" role="img" aria-label="Photo of a warm hotel lobby interior">
  <div class="label"><h4>Hotel 360 Operations</h4><p>Duis aute irure dolor in reprehen derit in voluptate</p></div>
</div>
<div class="service-card abs" style="left:319px;top:1276px;height:356px;background:linear-gradient(180deg,#6f5a4a 0%,#8fa3b0 35%,#b9c6c9 60%,#5c5550 100%)" role="img" aria-label="Photo of a hotel room opening onto a sea view">
  <div class="label"><h4>Hotel Budgeting</h4><p>Duis aute irure dolor in reprehen derit in voluptate</p></div>
</div>
<div class="service-card abs" style="left:609px;top:1307px;height:356px;background:linear-gradient(180deg,#2a2a2c 0%,#5a5a5c 45%,#2c2c2e 100%)" role="img" aria-label="Photo of a dark modern hotel bedroom">
  <div class="label"><h4>Business Plans</h4><p>Duis aute irure dolor in reprehen derit in voluptate</p></div>
</div>
<div class="service-card abs" style="left:899px;top:1276px;height:356px;background:linear-gradient(180deg,#d8d9dc 0%,#b9b6b2 45%,#6e6258 100%)" role="img" aria-label="Photo of a bright hotel restaurant dining room">
  <div class="label"><h4>Business Strategies</h4><p>Duis aute irure dolor in reprehen derit in voluptate</p></div>
</div>

<div class="services-band abs"></div>
<div class="abs" style="left:643px;top:1871px;width:557px;height:674px;background:linear-gradient(160deg,#a06a4e 0%,#7f6253 40%,#b8bec9 70%,#4a4e5e 100%)" role="img" aria-label="Photo of a smiling hotel manager holding a menu folder in a restaurant"></div>
<h2 class="heading abs" style="left:173px;top:1890px;font-size:27px">Our Hotel Services</h2>

<div class="service-item abs" style="top:1966px">
  <div class="item-icon"><svg width="36" height="36" viewBox="0 0 36 36" fill="none" stroke="#fff" stroke-width="1.6"><rect x="6" y="4" width="22" height="28"/><path d="M11 26V18M16 26V13M21 26V20"/></svg></div>
  <div><h5>Revenue Management</h5><p>Nemo enim ipsam voluptatem quia voluptas</p></div>
</div>
<div class="service-item abs" style="top:2071px">
  <div class="item-icon"><svg width="36" height="36" viewBox="0 0 36 36" fill="none" stroke="#fff" stroke-width="1.6"><circle cx="18" cy="9" r="5"/><path d="M8 32c0-8 4-14 10-14s10 6 10 14M10 20l-5-4M26 20l5-4"/></svg></div>
  <div><h5>Financial Advice</h5><p>Nemo enim ipsam voluptatem quia voluptas</p></div>
</div>
<div class="service-item abs" style="top:2176px">
  <div class="item-icon"><svg width="36" height="36" viewBox="0 0 36 36" fill="none" stroke="#fff" stroke-width="1.6"><circle cx="14" cy="10" r="6"/><path d="M4 30c0-7 4-11 10-11M18 22h14v10H18z"/></svg></div>
  <div><h5>Cost Management Solutions</h5><p>Nemo enim ipsam voluptatem quia voluptas</p></div>
</div>
<div class="service-item abs" style="top:2280px">
  <div class="item-icon"><svg width="36" height="36" viewBox="0 0 36 36" fill="none" stroke="#fff" stroke-width="1.6"><rect x="5" y="8" width="26" height="24"/><path d="M5 14h26M11 4v6M25 4v6M10 19h4M16 19h4M22 19h4M10 25h4M16 25h4"/></svg></div>
  <div><h5>Pre-Opening Hotel Overview</h5><p>Nemo enim ipsam voluptatem quia voluptas</p></div>
</div>

<h2 class="heading section-title abs center" style="left:0;top:2652px;width:1200px">Expertise in Hotel Management</h2>
<p class="lead abs center" style="left:170px;top:2706px;width:860px">Nemo enim ipsam voluptatem quia voluptas sit aspernatur aut odit aut fugit, sed quia consequuntur magni dolores eos qui ratione voluptatem sequi nesciunt.</p>

<div class="expert abs" style="left:174px;top:2825px;width:270px;height:270px;background:linear-gradient(135deg,#3c4150,#7a7f8a 50%,#2e3240)" role="img" aria-label="Photo of a team reviewing marketing plans"><span>Hotel<br>Marketing</span></div>
<div class="expert abs" style="left:453px;top:2813px;width:294px;height:294px;background:linear-gradient(135deg,#262d42,#3e465c 50%,#20273a)" role="img" aria-label="Photo of an investor meeting"><span>Investor<br>Communications<br>Support</span></div>
<div class="expert abs" style="left:756px;top:2825px;width:270px;height:270px;background:linear-gradient(135deg,#4a4c55,#a9a8a6 50%,#3a3c44)" role="img" aria-label="Photo of chefs working in a hotel kitchen"><span>Asset<br>Management</span></div>

<div class="contact-band abs"></div>
<div class="abs" style="left:0;top:3306px;width:593px;height:631px;background:linear-gradient(160deg,#b07a45 0%,#6e4e35 45%,#2a2522 100%)" role="img" aria-label="Photo of a smiling waiter holding a menu folder"></div>
<h2 class="heading abs" style="left:652px;top:3303px;font-size:27px">Contact Form</h2>
<div class="field abs" style="top:3373px">Name</div>
<div class="field abs" style="top:3441px">Phone</div>
<div class="field abs" style="top:3508px">Email</div>
<div class="abs" style="left:653px;top:3575px;font-size:13px;color:var(--ink)">Address</div>
<div class="field abs" style="top:3601px;height:96px;padding:0"></div>
<div class="submit abs">SUBMIT</div>

<footer class="footer abs">
  <div class="foot-icon abs" style="left:173px;top:171px"><svg width="30" height="30" viewBox="0 0 30 30" fill="none" stroke="#fff" stroke-width="1.6"><path d="M8 4l4 5-2 3c2 4 4 6 8 8l3-2 5 4-3 4C13 25 5 17 4 7z"/></svg></div>
  <div class="foot-icon abs" style="left:420px;top:171px"><svg width="26" height="32" viewBox="0 0 26 32" fill="none" stroke="#fff" stroke-width="1.6"><path d="M13 2C7 2 3 6 3 12c0 8 10 18 10 18s10-10 10-18c0-6-4-10-10-10z"/><circle cx="13" cy="12" r="4"/></svg></div>
  <div class="foot-title abs" style="left:173px;top:278px">Call us</div>
  <div class="foot-text abs" style="left:173px;top:310px">+ 61 8 5550 4127<br>info@pinnacresthm.com</div>
  <div class="foot-title abs" style="left:420px;top:278px">Address</div>
  <div class="foot-text abs" style="left:420px;top:312px">#45, Harbour View Lane,<br>Central Quay Road,<br>Australia, 600012,</div>
  <div class="foot-brand abs" style="left:661px;top:356px;width:400px">Pinnacrest Hotel Management<br>Consulting - Solutions</div>
  <div class="abs" style="left:173px;top:473px;width:1027px;height:1px;background:var(--line)"></div>
  <div class="foot-text abs center" style="left:0;top:508px;width:1200px">Copyrights @ 2021 Pinnacrest Hotel Management Consulting. All Rights Reserved</div>
</footer>

</body>
</html>
```